依頼詳細
◆ディナーショー詳細

・鳴瀬野ガーデンホテル(かつて天皇陛下も宿泊された、格式&レトロ感のあるホテル)にて開催。ディナーはフランス料理
・ショー第1部:二胡と箏(着物ドレス着用)(和風の音楽でスタート)
第2部:二胡とピアノ(カクテルドレス)
(生命の息吹を感じる季節・コロナも明けて・自身の九死に一生を得た体験を含めて、生きる歓びを語るようなトークを交えて)
第3部:二胡とソノリカ(トレーンの長いゴージャスなドレス)
(プロジェクターを使用し、画像や動画で世界観を演出)
・紅茶コンサルタントが、コース一品ずつに合わせ、料理に合う紅茶を提供
・ホテル本館2階ラウンジからは、海に浮かぶ「竹島」の絶景が眺められる。
17時よりラウンジにて、夕陽に染まる絶景を見ながらウェルカムドリンクを嗜んでいただく。
宴会場へ移動し、18時よりショースタート。
・桜の咲く時期を選んで開催

◆デザイン要望

・上記のディナーショーがイメージできるようなデザイン
もしくは
チラシを一枚見るだけで「どんなショーなのだろう?」とディナーショーへ期待の膨らむようなデザイン
(・・・でありながら、主役がぼけないチラシ)が希望です。
記載項目
掲載内容のテキストは、添付のエクセルファイルをご参照ください。ページ内に、宣材写真のダウンロードURLも貼ってありますので、写真はそこからご使用ください。(写真の使用枚数等こだわりはありません)
サイズ
A4
ページ数
片面
希望イメージ
シンプル 複雑
単色 カラフル
暗い 明るい
日常 高級
遊び心 厳粛
未来的 伝統的
女性的 男性的
希望する色
設定なし
納品ファイル
• 高解像度JPG (.jpg)
• PNG形式 (.png)
補足説明
・もし可能でしたら、印刷(コピエールやモナリト等)入稿まで行っていただくか、入稿方法をご指南いただけると助かります。印刷費用については、別途予算を組んでおります。
・今回依頼が初めてで不慣れな点が多々あります。ご不明な点やご指摘等ありましたら、仰っていただけますようよろしくお願いいたします。
■ 選んだ理由

素敵な作品を沢山ご提案いただき、私としては絞りきれず、とても迷ってしまいました。そこで、家族やディナーショーの協力者、スタッフなど、複数の方に相談したところ、多数決で柚木様のデザインに票が集まり、決定させていただきました。全体的に優しい色味で文字も見やすく、気に入っています。

■ 提案者全員のお礼・コメント

この度は沢山のご提案をいただき、本当にありがとうございました。ご提案をいただく度に、A4用紙一枚に込められたデザインの多様性やデザイナーさんの思い、一瞬にしてインパクトを与えるチラシデザインの奥深さに感動して、何度か目が潤んでしまいました。できれば部屋に飾っておきたい作品もありましたが、そういう選択ができないのが残念です。また依頼させていただく際には、よろしくお願い致します。

```html
<!DOCTYPE html>
<html lang="ja">
<head>
<meta charset="utf-8">
<title>東雲 美織 スプリングディナーショー</title>
<link rel="stylesheet" href="https://fonts.googleapis.com/css2?family=Shippori+Mincho:wght@500;700;800&display=swap">
<style>
  :root{
    --sky-top:#6f5a86;
    --sky-mid:#c98a9c;
    --sky-glow:#f0a36a;
    --sun:#ffd59a;
    --sea:#2c2435;
    --sea-deep:#1a1624;
    --blossom:#f4c6d2;
    --blossom-deep:#e49ab0;
    --performer:#d9cbc6;
    --title:#5a1a2e;
    --white:#ffffff;
    --panel:rgba(255,255,255,0.82);
    --panel-text:#2a1a22;
  }
  *{margin:0;padding:0;box-sizing:border-box}
  html,body{width:854px;height:1200px;overflow:hidden;background:var(--sea-deep)}
  .flyer{position:relative;width:854px;height:1200px;overflow:hidden;
    font-family:"Shippori Mincho",serif;color:var(--title)}
  .backdrop{position:absolute;inset:0;
    background:
      radial-gradient(ellipse 420px 120px at 430px 745px, var(--sun) 0%, rgba(255,200,120,.6) 35%, rgba(240,163,106,0) 75%),
      linear-gradient(180deg,var(--sky-top) 0%,#9d7a9f 18%,var(--sky-mid) 38%,#e29b86 55%,var(--sky-glow) 62%,#b7667a 64%,var(--sea) 72%,var(--sea-deep) 100%)}
  .blossoms{position:absolute;left:380px;top:0;width:474px;height:300px;
    background:radial-gradient(ellipse at 70% 30%,var(--blossom) 0%,var(--blossom-deep) 40%,rgba(228,154,176,0) 72%);opacity:.9}
  .performer{position:absolute;left:500px;top:330px;width:300px;height:520px;border-radius:140px 140px 40px 40px;
    background:linear-gradient(180deg,rgba(120,80,80,.55) 0%,var(--performer) 35%,rgba(217,203,198,.35) 100%)}
  .headline{position:absolute;left:40px;top:98px;font-weight:800;line-height:1.15}
  .artist{font-size:54px;letter-spacing:4px}
  .show-title{font-size:46px;margin-top:24px;letter-spacing:1px}
  .show-date{font-size:50px;margin-top:20px}
  .tagline{position:absolute;left:134px;top:392px;color:var(--white);font-size:21px;line-height:41px;font-weight:500;
    text-shadow:0 0 6px rgba(0,0,0,.4)}
  .tagline p:nth-child(3){margin-left:0}
  .venue{position:absolute;left:40px;top:748px;color:var(--white);font-size:32px;font-weight:700;letter-spacing:2px}
  .schedule{position:absolute;left:40px;top:808px;width:720px;padding:16px 22px;background:var(--panel);
    color:var(--panel-text);font-size:25px;font-weight:700;line-height:42px}
  .schedule .row{display:flex;white-space:nowrap}
  .schedule .label{width:236px}
  .schedule .time{width:150px}
  .schedule .place{font-size:20px;align-self:center}
  .contact{position:absolute;left:40px;top:1010px;color:var(--white);font-size:25px;font-weight:700;line-height:40px}
  .brand{position:absolute;left:640px;top:1000px;width:120px;height:120px;border-radius:50%;
    border:2px solid var(--white);display:flex;align-items:center;justify-content:center;
    color:var(--white);font-size:20px;font-weight:700;text-align:center;line-height:1.3}
</style>
</head>
<body>
<div class="flyer">
  <div class="backdrop" role="img" aria-label="海に浮かぶ竹島と夕陽に染まる空の写真"></div>
  <div class="blossoms" role="img" aria-label="満開の桜の枝の写真"></div>
  <div class="performer" role="img" aria-label="白いドレスで二胡を演奏する演奏者の写真"></div>

  <header class="headline">
    <h1 class="artist">東雲　美織</h1>
    <p class="show-title">スプリングディナーショー</p>
    <p class="show-date">2022年4月3日（日）</p>
  </header>

  <div class="tagline">
    <p>咲き誇るさくら</p>
    <p>夕陽に染まる竹島</p>
    <p>数々の出会いを一期一会の音色で</p>
    <p>あなたを二胡の世界へ誘います</p>
  </div>

  <p class="venue">鳴瀬野ガーデンホテル</p>

  <section class="schedule">
    <div class="row"><span class="label">ウェルカムドリンク</span><span class="time">17:00〜</span><span class="place">本館メインダイニングルーム</span></div>
    <div class="row"><span class="label">ショー＆ディナー</span><span class="time">18:00〜</span><span class="place">別館バンケットホール</span></div>
    <div class="row"><span>お一人様 ¥27,000（税、サービス料込）</span></div>
  </section>

  <section class="contact">
    <p>【ご予約・お問い合わせ】</p>
    <p>(080)3917-2486</p>
    <p>shinonome-miori.jp/contact/</p>
  </section>

  <div class="brand">MIORI<br>SHINONOME</div>
</div>
</body>
</html>
```